Stellenausschreibungen für Dachdeckerbetrieb
Zielgruppe
Wir sind ein Dachdeckerbetrieb und suchen verstärkt nach Zuwachs.
Aufgabenstellung
Die Stellenausschreibungen soll schlicht und modern sein. Eine Seite, beidseitig bedruckt ist völlig ausreichend. Detailreiche, ansprechende Bilder zu unserem Dachdecker Gewerk sind erwünscht.

```html
<!DOCTYPE html>
<html lang="de">
<head>
<meta charset="utf-8">
<title>Stellenausschreibung Kastendorn</title>
<link href="https://fonts.googleapis.com/css2?family=Didact+Gothic&display=swap" rel="stylesheet">
<style>
:root{
  --green:#0f9a48;
  --paper:#f3f3f1;
  --ink:#1d1d1b;
  --stage:#d8d8d6;
  --roof-a:#b9704a;
  --roof-b:#5d7088;
}
*{box-sizing:border-box;margin:0;padding:0}
html,body{width:1200px;height:750px;overflow:hidden}
body{background:var(--stage);font-family:"Didact Gothic",Arial,sans-serif;color:var(--ink);position:relative}
.card{position:absolute;top:173px;width:570px;height:404px;background:var(--paper);overflow:hidden;box-shadow:0 2px 6px rgba(0,0,0,.18)}
.front{left:20px}
.back{left:610px;background:var(--green)}

/* front */
.front .company{position:absolute;left:26px;top:26px;color:var(--green);font-size:21px;line-height:1.15;font-weight:400}
.front .brand{position:absolute;left:272px;top:32px;display:flex;align-items:center;gap:7px;color:var(--green);font-size:19px}
.brand .mark{width:14px;height:14px;background:currentColor}
.front .rule{position:absolute;left:0;top:92px;width:405px;height:5px;background:var(--green)}
.front .headline{position:absolute;left:32px;top:104px;color:var(--green);font-size:20px;font-style:italic;font-weight:400}
.front .intro{position:absolute;left:32px;top:134px;width:350px;font-size:9.5px;line-height:1.35}
.front .jobs{position:absolute;left:72px;top:188px;font-size:9.5px;line-height:1.35;list-style:none}
.front .jobs li::before{content:"• ";color:var(--green)}
.front .note{position:absolute;left:40px;top:244px;width:330px;font-size:9.5px;line-height:1.35}
.front .photos{position:absolute;right:0;top:0;width:165px;height:292px;display:flex;flex-direction:column;gap:6px;background:var(--green)}
.photos .photo{flex:1}
.photo.p1{background:linear-gradient(160deg,#8a8f96,#4b5057)}
.photo.p2{background:linear-gradient(160deg,#9fb0c4,#5a4c44)}
.photo.p3{background:linear-gradient(160deg,var(--roof-b),#c9a67a)}
.photo.p4{background:linear-gradient(160deg,#6a5a4e,var(--roof-a))}
.band{position:absolute;left:0;bottom:0;width:100%;background:var(--green);color:#fff;text-align:center}
.front .band{height:112px;padding-top:28px;font-size:12px;line-height:1.35}
.front .band .web{position:absolute;left:0;top:-18px;width:405px;color:var(--green);font-size:12px}

/* back */
.back .brand{position:absolute;left:26px;top:24px;display:flex;align-items:center;gap:7px;color:#fff;font-size:19px}
.back .divider{position:absolute;left:0;top:86px;width:175px;height:3px;background:#fff}
.services{position:absolute;left:28px;top:108px;list-style:none;color:#fff;font-size:11.5px;line-height:2.4}
.back .panel{position:absolute;left:175px;top:0;width:395px;height:300px;background:var(--paper);padding:14px 14px 8px 16px;display:flex;flex-direction:column}
.columns{display:grid;grid-template-columns:1fr 1fr;column-gap:14px;row-gap:10px;align-content:start}
.block h3{font-weight:400;font-size:10px;margin-bottom:3px}
.block ul{list-style:none;font-size:8.2px;line-height:1.28;padding-left:8px}
.block li::before{content:"• ";color:var(--green)}
.back .apply{margin-top:auto;color:var(--green);font-size:10.5px;line-height:1.3;text-align:center}
.back .band{height:104px;left:175px;width:395px;padding-top:20px;font-size:12px;line-height:1.35;background:transparent}
</style>
</head>
<body>

<section class="card front">
  <h1 class="company">Kastendorn Dach- und<br>Gründachbau GmbH</h1>
  <div class="brand"><span class="mark"></span>Kastendorn</div>
  <div class="rule"></div>
  <h2 class="headline">Wir haben freie Stellen</h2>
  <p class="intro">Wir sind ein Familienunternehmen mit Sitz in Musterstadt. In den vergangenen 29 Jahren sind wir gewachsen – und es gibt einiges zu tun! Für unsere vielfältigen Projekte suchen wir:</p>
  <ul class="jobs">
    <li>Dachdeckerhelfer (m/w)</li>
    <li>Vorarbeiter (m/w) im Bereich Kundendienst</li>
    <li>Abdichter (m/w) im Bereich Flachdach</li>
  </ul>
  <p class="note">Unsere Vorstellungen und was Sie von uns erwarten können, finden Sie auf der Rückseite.</p>
  <div class="photos">
    <div class="photo p1" role="img" aria-label="Foto: Dachdecker bei der Arbeit auf einem Flachdach"></div>
    <div class="photo p2" role="img" aria-label="Foto: Handwerker mit Werkzeug am Dachrand"></div>
    <div class="photo p3" role="img" aria-label="Foto: Dachdecker auf einem Dach mit Lattung und Folie"></div>
    <div class="photo p4" role="img" aria-label="Foto: Dachfenster zwischen roten Biberschwanzziegeln"></div>
  </div>
  <div class="band">
    <div class="web">www.kastendorn-dach.de</div>
    Lindenpfad 12 • 55000 Musterstadt<br>
    Telefon: 06100 - 4420 - 0<br>
    E-Mail: info@kastendorn-dach.de
  </div>
</section>

<section class="card back">
  <div class="brand"><span class="mark"></span>Kastendorn</div>
  <div class="divider"></div>
  <ul class="services">
    <li>Flachdachabdichtung</li>
    <li>Dachdeckerarbeiten</li>
    <li>Schieferarbeiten</li>
    <li>Spenglerarbeiten</li>
    <li>Dachfenster</li>
    <li>Wartung</li>
    <li>Reparaturarbeiten</li>
  </ul>
  <div class="panel">
    <div class="columns">
      <div class="block">
        <h3>Zu Ihren neuen Tätigkeiten gehören...</h3>
        <ul>
          <li>Dachdeckerarbeiten am Neubau und Bestand</li>
          <li>Aufmaß vor Ort erstellen</li>
          <li>Steildach/Flachdach, Sanierung oder Neubau mit Ziegel oder Betondachsteinen</li>
          <li>Dachflächenfenster</li>
          <li>Reparatur und Wartung</li>
        </ul>
      </div>
      <div class="block">
        <h3>Was wir von Ihnen erwarten...</h3>
        <ul>
          <li>Selbstständiges Ausführen von Projektarbeiten aller Art, Reparatur- und Wartungsaufträgen</li>
          <li>Unterstützung bei Dachdecker- und Klempnerarbeiten</li>
          <li>Vorbereitungen von Projektarbeiten anhand von Leistungsverzeichnissen und Zeichnungen</li>
        </ul>
      </div>
      <div class="block">
        <h3>Was Sie mitbringen...</h3>
        <ul>
          <li>Sie haben eine erfolgreiche Ausbildung in einem handwerklichen Beruf abgeschlossen</li>
          <li>Sie haben eine erfolgreiche Ausbildung als Dachdeckergeselle abgeschlossen</li>
          <li>Sie besitzen eine gültige Fahrerlaubnis der Führerscheinklasse BE (früher 3)</li>
          <li>Sie besitzen vorzugsweise Berufserfahrung</li>
          <li>Ihr Kommunikationsverhalten – Sie treten freundlich und sicher auf</li>
        </ul>
      </div>
      <div class="block">
        <h3>Was Sie von uns erwarten können...</h3>
        <ul>
          <li>Leistungsorientierte, pünktliche und korrekte Bezahlung Ihrer Leistung, dazu gehören selbstverständlich auch Urlaubs- und Weihnachtsgeld</li>
          <li>Stellung von Arbeitskleidung</li>
          <li>Angenehmes Arbeitsklima in einem tollen Team</li>
          <li>Stetige Weiterbildung</li>
        </ul>
      </div>
    </div>
    <p class="apply">Richten Sie Ihre Bewerbung bitte an info@kastendorn-dach.de<br>www.kastendorn-dach.de</p>
  </div>
  <div class="band">
    Lindenpfad 12 • 55000 Musterstadt<br>
    Telefon: 06100 - 4420 - 0<br>
    E-Mail: info@kastendorn-dach.de
  </div>
</section>

</body>
</html>
```